SkyRavelin Unique Gift Certificate

We need a unique, luxury gift certificate created for our online company (SkyRavelin). We are looking for something out of the ordinary, ie. do not want it to look like a 'normal' gift certificate. Please visit our website to gain a feel for our company (skyravelin.com.au). The dimensions are 148x148mm. We need our logo, website details, to, from, description, code, exp date included. The certificate will be printed on wood veneer so watermarks will not work. We want it to be clean and minimalistic.

Industry/Entity Type

It Company

```html
<!DOCTYPE html>
<html lang="en">
<head>
<meta charset="utf-8">
<title>SkyRavelin Gift Certificate</title>
<link rel="stylesheet" href="https://fonts.googleapis.com/css2?family=Overlock:wght@400;700&display=swap">
<style>
  :root {
    --teal: #2a8aa6;
    --teal-soft: rgba(120, 190, 205, 0.22);
    --ink: #1f1f1f;
    --edge: #3a3a3a;
    --paper: #ffffff;
    --lettering: rgba(40, 40, 40, 0.07);
  }
  html, body {
    margin: 0;
    padding: 0;
    width: 1200px;
    height: 1200px;
    overflow: hidden;
    background: var(--paper);
  }
  .certificate {
    position: relative;
    width: 1200px;
    height: 1200px;
    box-sizing: border-box;
    border: 2px solid var(--edge);
    background: var(--paper);
    font-family: "Overlock", sans-serif;
    color: var(--ink);
    overflow: hidden;
  }
  .wash {
    position: absolute;
    inset: 0;
    background:
      radial-gradient(ellipse 260px 180px at 760px 720px, var(--teal-soft), transparent 70%),
      radial-gradient(ellipse 220px 260px at 300px 900px, var(--teal-soft), transparent 70%),
      radial-gradient(ellipse 240px 160px at 980px 300px, var(--teal-soft), transparent 70%),
      radial-gradient(ellipse 200px 200px at 620px 1060px, var(--teal-soft), transparent 70%),
      radial-gradient(ellipse 120px 140px at 80px 560px, rgba(245, 225, 120, 0.18), transparent 70%),
      radial-gradient(ellipse 80px 160px at 1190px 520px, rgba(200, 150, 200, 0.2), transparent 70%);
  }
  .frame {
    position: absolute;
    left: 22px;
    top: 22px;
    width: 1154px;
    height: 1154px;
    border: 4px solid var(--teal);
  }
  .brand-name {
    position: absolute;
    left: 64px;
    top: 306px;
    width: 300px;
    text-align: center;
    font-size: 50px;
    font-weight: 700;
    line-height: 1;
    color: var(--ink);
  }
  .website {
    position: absolute;
    left: 62px;
    top: 403px;
    font-size: 24px;
    line-height: 1.2;
    color: var(--ink);
  }
  .headline {
    position: absolute;
    left: 528px;
    top: 80px;
    width: 536px;
    height: 280px;
    background: var(--lettering);
    border-radius: 24px;
  }
  .field-label {
    position: absolute;
    font-size: 51px;
    line-height: 1;
    white-space: nowrap;
  }
  .label-right { right: 878px; }
  .field-box {
    position: absolute;
    box-sizing: border-box;
    border: 2.5px solid var(--teal);
    background: rgba(255, 255, 255, 0.55);
  }
</style>
</head>
<body>
  <main class="certificate">
    <div class="wash" role="img" aria-label="Soft watercolour wash in pale teal"></div>
    <div class="frame"></div>

    <div class="brand-name">SkyRavelin</div>
    <div class="website">www.skyravelin.com.au</div>

    <div class="headline" role="img" aria-label="Hand-lettered heading: A gift for you!"></div>

    <span class="field-label label-right" style="top:512px;">A gift to</span>
    <div class="field-box" style="left:332px; top:508px; width:776px; height:83px;"></div>

    <span class="field-label label-right" style="top:608px;">Description</span>
    <div class="field-box" style="left:332px; top:606px; width:776px; height:152px;"></div>

    <span class="field-label label-right" style="top:770px;">From</span>
    <div class="field-box" style="left:332px; top:772px; width:776px; height:83px;"></div>

    <span class="field-label" style="left:332px; top:902px;">Code</span>
    <div class="field-box" style="left:328px; top:960px; width:349px; height:84px;"></div>

    <span class="field-label" style="left:763px; top:898px;">Expiration date</span>
    <div class="field-box" style="left:760px; top:960px; width:349px; height:84px;"></div>
  </main>
</body>
</html>
```